Social Media Graphics - Harbor Climb REVISED

Create 6-7 individual social media graphics (square size) to encourage folks to join our online course called:

The Lantern Ledger Plan
How to Launch a Multi-Million Business From Scratch
Sign Up Today!

IMPORTANT: Make the largest and most prominent text on the graphic be: How to Launch a Multi-Million Business From Scratch

For the color scheme of the graphics, let's try a blue color palette; make sure the graphics appeal to both men and women

Make sure each graphic contains 1 of the 3 pics attached (crop pic as needed); and make sure one of the graphics is all TEXT only.

Target Market(s)

men and women looking to start a business

Industry/Entity Type

Entrepreneurship

Colors
0054AA
0677BA
7BADD7
CADEEF
E8F1F8

Requirements
Must have
• All the text and use the 3 pics provided; one graphic can be all text; Simple, modern design that's easy to read

```html
<!DOCTYPE html>
<html lang="en">
<head>
<meta charset="utf-8">
<title>The Lantern Ledger Plan – Social Graphic</title>
<link rel="stylesheet" href="https://fonts.googleapis.com/css2?family=Anton&display=swap">
<style>
  :root {
    --bg-deep: #0b426f;
    --bg-mid: #0f6aa6;
    --bg-light: #1e93d4;
    --panel: #1e1e3f;
    --panel-rule: #3f8fce;
    --accent: #4aa3dc;
    --white: #ffffff;
    --photo-a: #1b2a3c;
    --photo-b: #2a5c8f;
  }
  * { margin: 0; padding: 0; box-sizing: border-box; }
  html, body { width: 1200px; height: 1200px; overflow: hidden; }
  body { font-family: "Anton", "Oswald", sans-serif; }
  .graphic {
    position: relative;
    width: 1200px;
    height: 1200px;
    overflow: hidden;
    background:
      radial-gradient(ellipse 70% 60% at 78% 30%, var(--bg-light) 0%, var(--bg-mid) 50%, transparent 85%),
      radial-gradient(ellipse 60% 50% at 72% 88%, #1a87c8 0%, transparent 70%),
      var(--bg-deep);
  }
  .graphic svg { position: absolute; inset: 0; }
  .type { font-family: "Anton", "Oswald", sans-serif; fill: var(--white); }
  .signup { fill: var(--accent); letter-spacing: 6px; }
  .hosts-photo {
    position: absolute;
    left: 492px;
    top: 108px;
    width: 576px;
    height: 440px;
    border-radius: 200px 200px 0 0;
    background: linear-gradient(180deg, var(--photo-b) 0%, var(--photo-a) 60%, #1f4f83 100%);
  }
</style>
</head>
<body>
<main class="graphic">
  <div class="hosts-photo" role="img" aria-label="Photo of the two course hosts smiling, a man in a black turtleneck with arms crossed and a woman in a blue denim jacket"></div>

  <svg width="1200" height="1200" viewBox="0 0 1200 1200" aria-hidden="false">
    <g class="course-title">
      <text class="type" x="102" y="230" font-size="134" textLength="183" lengthAdjust="spacingAndGlyphs">THE</text>
      <text class="type" x="100" y="370" font-size="134" textLength="380" lengthAdjust="spacingAndGlyphs">LANTERN</text>
      <text class="type" x="96" y="497" font-size="104" textLength="388" lengthAdjust="spacingAndGlyphs">LEDGER PLAN</text>
    </g>

    <g class="headline-panel">
      <rect x="58" y="547" width="1032" height="461" rx="22" fill="var(--panel)"/>
      <rect x="76" y="565" width="996" height="425" rx="16" fill="none" stroke="var(--panel-rule)" stroke-width="1.5"/>
      <rect x="81" y="570" width="986" height="415" rx="13" fill="none" stroke="var(--panel-rule)" stroke-width="1"/>
      <text class="type" x="140" y="715" font-size="145" textLength="880" lengthAdjust="spacingAndGlyphs">HOW TO LAUNCH</text>
      <text class="type" x="140" y="852" font-size="145" textLength="880" lengthAdjust="spacingAndGlyphs">A MULTI-MILLION</text>
      <text class="type" x="136" y="956" font-size="104" textLength="880" lengthAdjust="spacingAndGlyphs">BUSINESS FROM SCRATCH</text>
    </g>

    <g class="call-to-action">
      <line x1="58" y1="1072" x2="410" y2="1072" stroke="var(--accent)" stroke-width="3"/>
      <line x1="738" y1="1072" x2="1090" y2="1072" stroke="var(--accent)" stroke-width="3"/>
      <text class="type signup" x="574" y="1093" font-size="52" text-anchor="middle" textLength="292" lengthAdjust="spacingAndGlyphs">SIGN UP TODAY</text>
    </g>
  </svg>
</main>
</body>
</html>
```